Property Management business needs Business cards designed

We provide a premium property management service based in Sydney's Norther Beaches. We want people to feel confident in choosing us to manage their investment properties. We offer a much more personalized service than other estate agents.
We want a modern clean design. Something that shows confidence without being complicated.
Logo attached.

Target Market(s)

35-70yo Male and Female with strong property portfolios within Sydney's Norther Beaches

Industry/Entity Type

Property Management

Contact Information for Business Card

Address: Suite 7, 18-19 Harlow Parade, Manly NSW 2095
Two separate named cards.
Tom Carver - 0413 572 961 tom@harlowlettings.com.au
Marisol Ketter - 0408 167 543 marisol@harlowlettings.com.au

Requirements
Must have
• Business logo, name, number, address, email.

```html
<!DOCTYPE html>
<html lang="en">
<head>
<meta charset="UTF-8">
<title>Harlow Lettings – Business Card</title>
<link href="https://fonts.googleapis.com/css2?family=Roboto:wght@400;700&display=swap" rel="stylesheet">
<style>
  :root {
    --backdrop: #d8dbde;
    --card-white: #ffffff;
    --stripe-cream: #e6e1cf;
    --teal-light: #1f8c93;
    --teal-mid: #137a84;
    --teal-deep: #0d6670;
    --ink-dark: #1b1f24;
    --text-light: #ffffff;
    --icon-tint: #9fd6da;
  }
  html, body {
    margin: 0;
    padding: 0;
    width: 1200px;
    height: 1200px;
    overflow: hidden;
    background: var(--backdrop);
  }
  .canvas {
    position: relative;
    width: 1200px;
    height: 1200px;
  }
  .business-card {
    position: absolute;
    left: 100px;
    top: 314px;
    width: 1000px;
    height: 572px;
    border-radius: 4px;
    overflow: hidden;
    box-shadow: 0 10px 30px rgba(0, 0, 0, 0.18);
    font-family: "Roboto", Arial, sans-serif;
  }
  .card-shapes {
    position: absolute;
    inset: 0;
    width: 100%;
    height: 100%;
  }
  .brand-mark {
    position: absolute;
    right: 70px;
    top: 78px;
    display: flex;
    align-items: center;
    gap: 16px;
  }
  .brand-dot {
    width: 30px;
    height: 30px;
    border-radius: 50%;
    background: var(--teal-mid);
  }
  .brand-name {
    font-weight: 700;
    font-size: 40px;
    letter-spacing: 1px;
    color: var(--ink-dark);
    text-transform: uppercase;
  }
  .contact-block {
    position: absolute;
    left: 72px;
    top: 272px;
    color: var(--text-light);
  }
  .person-name {
    margin: 0 0 18px;
    font-weight: 700;
    font-size: 36px;
    line-height: 1.1;
  }
  .contact-list {
    list-style: none;
    margin: 0;
    padding: 0;
  }
  .contact-item {
    display: flex;
    align-items: flex-start;
    gap: 18px;
    margin-bottom: 14px;
    font-weight: 400;
    font-size: 24px;
    line-height: 1.25;
  }
  .contact-icon {
    flex: 0 0 26px;
    width: 26px;
    height: 26px;
    margin-top: 2px;
  }
</style>
</head>
<body>
<div class="canvas">
  <article class="business-card">
    <svg class="card-shapes" viewBox="0 0 1000 572" preserveAspectRatio="none" aria-hidden="true">
      <defs>
        <linearGradient id="teal-field" x1="0" y1="0" x2="1" y2="1">
          <stop offset="0" stop-color="var(--teal-light)"/>
          <stop offset="0.55" stop-color="var(--teal-mid)"/>
          <stop offset="1" stop-color="var(--teal-deep)"/>
        </linearGradient>
      </defs>
      <rect class="card-base" width="1000" height="572" fill="var(--card-white)"/>
      <polygon class="cream-stripe" points="200,0 1000,488 1000,572 0,572 0,0" fill="var(--stripe-cream)"/>
      <polygon class="teal-field" points="186,0 1000,500 1000,572 0,572 0,0" fill="url(#teal-field)"
               role="img" aria-label="Faceted teal geometric background"/>
    </svg>

    <div class="brand-mark">
      <span class="brand-dot"></span>
      <span class="brand-name">Harlow Lettings</span>
    </div>

    <div class="contact-block">
      <h1 class="person-name">Tom Carver</h1>
      <ul class="contact-list">
        <li class="contact-item">
          <svg class="contact-icon" viewBox="0 0 26 26" aria-hidden="true">
            <rect x="7" y="2" width="12" height="22" rx="2" fill="none" stroke="var(--icon-tint)" stroke-width="2"/>
            <line x1="11" y1="20" x2="15" y2="20" stroke="var(--icon-tint)" stroke-width="2"/>
          </svg>
          <span>0413 572 961</span>
        </li>
        <li class="contact-item">
          <svg class="contact-icon" viewBox="0 0 26 26" aria-hidden="true">
            <rect x="2" y="5" width="22" height="16" rx="1.5" fill="var(--icon-tint)"/>
            <polyline points="3,6 13,14 23,6" fill="none" stroke="var(--teal-mid)" stroke-width="2"/>
          </svg>
          <span>tom@harlowlettings.com.au</span>
        </li>
        <li class="contact-item">
          <svg class="contact-icon" viewBox="0 0 26 26" aria-hidden="true">
            <polygon points="3,5 23,5 13,22" fill="var(--icon-tint)"/>
          </svg>
          <span>Suite 7, 18-19 Harlow Parade,<br>Harlow Bay NSW 2199</span>
        </li>
      </ul>
    </div>
  </article>
</div>
</body>
</html>
```